New residential property management company

I have a lot of name recognition in our smaller town due to owning a construction company here. I have now started a residential property management company representing landlords and tenants. Just trying to get my name out there and get some rentals to manage!

```html
<!DOCTYPE html>
<html lang="en">
<head>
<meta charset="utf-8">
<title>Hollis Property Management – Postcard</title>
<link rel="stylesheet" href="https://fonts.googleapis.com/css2?family=Montserrat:wght@400;500;600;700;800;900&family=Bebas+Neue&display=swap">
<style>
:root{
  --ink:#262626;
  --ink-soft:#3a3a3a;
  --grey:#8d8d8d;
  --grey-light:#a3a3a3;
  --paper:#ffffff;
  --canvas:#eeeeee;
}
*{margin:0;padding:0;box-sizing:border-box}
html,body{width:1200px;height:2371px;overflow:hidden;background:var(--canvas)}
body{position:relative;font-family:'Montserrat',sans-serif;color:var(--ink)}
.card{position:absolute;left:80px;width:1040px;background:var(--paper);box-shadow:0 14px 28px rgba(0,0,0,.22);overflow:hidden}
.card--front{top:380px;height:695px}
.card--back{top:1300px;height:691px}
.card__inner{position:absolute;left:0;top:0;width:768px;height:513px;transform:scale(1.3542);transform-origin:0 0}
.card--back .card__inner{height:510px}
.abs{position:absolute}
.shapes{position:absolute;left:0;top:0}

/* brand */
.brand{display:flex;align-items:center;gap:12px}
.brand__mark{width:44px;height:44px;background:var(--ink)}
.brand__name{font-weight:600;color:var(--ink);line-height:1;letter-spacing:1px}
.brand__name small{display:block;font-size:8px;letter-spacing:2.4px;margin-top:4px;font-weight:600}

/* front */
.headline{left:38px;top:115px;color:#fff}
.headline__lead{font-size:19px;font-weight:400;line-height:22px;letter-spacing:-.2px}
.headline__big{font-size:37px;font-weight:900;line-height:46px;letter-spacing:-.5px}
.intro{left:38px;top:224px;width:320px;border-left:3px solid var(--ink);padding-left:12px;font-size:11.5px;line-height:14px;color:var(--ink-soft)}
.perk{top:280px;width:110px;text-align:center;font-size:13px;font-weight:600;line-height:16px}
.perk__icon{width:50px;height:50px;border-radius:50%;background:var(--grey);margin:0 auto 8px;display:flex;align-items:center;justify-content:center}
.divider{top:282px;height:50px;border-left:1.5px dotted var(--ink)}
.services-title{left:38px;top:382px;color:#fff;font-size:15px;font-weight:700}
.service-list{top:414px;list-style:none;font-size:12px;font-weight:500;line-height:18.5px}
.service-list li{display:flex;align-items:center;gap:8px}
.tick{width:9px;height:9px;flex:none}
.contact-strip{left:36px;top:485px;color:#fff;font-size:11px;font-weight:500;display:flex;align-items:center;gap:8px}
.contact-strip .sep{width:1px;height:14px;background:#fff}
.person{left:0;top:0}
.offer{left:492px;top:305px;width:222px;height:153px;background:var(--ink);border-radius:10px;color:#fff;text-align:center}
.offer__title{font-family:'Bebas Neue',sans-serif;font-size:44px;line-height:38px;margin-top:12px;letter-spacing:.3px}
.offer__rule{width:176px;height:2px;background:#fff;margin:8px auto 6px}
.offer__sub{font-size:21px;font-weight:700;letter-spacing:.5px}
.offer__sub sup{font-size:11px}
.agent{left:494px;top:466px;font-size:25px;font-weight:800;letter-spacing:.4px}

/* back */
.back-title{left:40px;top:24px;color:#fff;font-size:24px;font-weight:400;letter-spacing:-.2px}
.role-list{top:60px;list-style:none;color:#fff;font-size:12px;font-weight:500;line-height:19px}
.role-list li{display:flex;align-items:center;gap:8px}
.back-cta{left:40px;top:126px;color:#fff;font-size:27px;font-weight:900;line-height:28px}
.estimate-pill{left:22px;top:437px;width:150px;height:20px;border-radius:10px;background:var(--grey-light);color:#fff;font-size:11px;font-weight:700;text-align:center;line-height:20px;letter-spacing:.5px}
.estimate-label{left:35px;top:458px;color:#fff;font-family:'Bebas Neue',sans-serif;font-size:33px;letter-spacing:.3px}
.back-phone{left:208px;top:442px;font-size:27px;font-weight:600;display:flex;align-items:center;gap:8px}
.back-mail{left:210px;top:479px;font-size:13px;font-weight:500;display:flex;align-items:center;gap:9px}
.stamp{left:662px;top:25px;width:69px;height:69px;border:1.5px solid var(--ink)}
</style>
</head>
<body>

<!-- FRONT -->
<section class="card card--front">
  <div class="card__inner">
    <svg class="shapes" width="768" height="513" viewBox="0 0 768 513">
      <defs>
        <linearGradient id="frontPhoto" x1="0" y1="0" x2="0" y2="1">
          <stop offset="0" stop-color="#a7b6d4"/>
          <stop offset=".45" stop-color="#8c8f96"/>
          <stop offset=".75" stop-color="#6f8f45"/>
          <stop offset="1" stop-color="#5b7f36"/>
        </linearGradient>
      </defs>
      <circle cx="625" cy="50" r="276" fill="var(--ink)"/>
      <circle cx="610" cy="58" r="262" fill="url(#frontPhoto)" role="img" aria-label="Photo of a large two-storey suburban home with a green lawn at dusk"/>
      <polygon points="0,103 366,103 392,217 0,217" fill="var(--ink)"/>
      <polygon points="0,377 372,377 378,405 0,405" fill="var(--ink)"/>
      <polygon points="0,474 372,474 372,513 0,513" fill="var(--ink)"/>
    </svg>

    <div class="abs brand" style="left:60px;top:26px">
      <span class="brand__mark"></span>
      <span class="brand__name" style="font-size:46px">HOLLIS<small>PROPERTY MANAGEMENT LLC.</small></span>
    </div>

    <div class="abs headline">
      <p class="headline__lead">DOES PROPERTY OWNERSHIP<br>FEEL LIKE A SECOND JOB?</p>
      <p class="headline__big">WE CAN HELP!</p>
    </div>

    <p class="abs intro">It is a long established fact that a reader will be distracted by the readable content of a page when looking at its layout.</p>

    <div class="abs perk" style="left:25px">
      <div class="perk__icon"><svg width="26" height="26" viewBox="0 0 26 26" fill="none" stroke="#222" stroke-width="1.8"><circle cx="13" cy="11" r="8"/><path d="M9 11l3 3 5-6"/><path d="M8 18l-2 6 4-2 2 3M18 18l2 6-4-2-2 3"/></svg></div>
      Guaranteed<br>Rent
    </div>
    <span class="abs divider" style="left:136px"></span>
    <div class="abs perk" style="left:129px">
      <div class="perk__icon"><svg width="24" height="26" viewBox="0 0 24 26" fill="none" stroke="#222" stroke-width="1.8"><path d="M4 2h16M4 24h16M6 2c0 7 12 7 12 11S6 17 6 24M18 2c0 7-12 7-12 11s12 4 12 11"/></svg></div>
      Long Term<br>Appreciation
    </div>
    <span class="abs divider" style="left:241px"></span>
    <div class="abs perk" style="left:231px">
      <div class="perk__icon"><svg width="26" height="24" viewBox="0 0 26 24" fill="none" stroke="#222" stroke-width="1.8"><path d="M3 12L13 3l10 9M6 10v11h14V10"/><path d="M10 21v-6h6v6"/></svg></div>
      No<br>Headaches
    </div>

    <p class="abs services-title">Comprehensive Service include:</p>
    <ul class="abs service-list" style="left:38px">
      <li><svg class="tick" viewBox="0 0 10 10" fill="none" stroke="#444" stroke-width="1"><rect x=".5" y=".5" width="8" height="8"/><path d="M2.5 5l2 2 4-5"/></svg>24/7 Maintenance</li>
      <li><svg class="tick" viewBox="0 0 10 10" fill="none" stroke="#444" stroke-width="1"><rect x=".5" y=".5" width="8" height="8"/><path d="M2.5 5l2 2 4-5"/></svg>Leasing</li>
      <li><svg class="tick" viewBox="0 0 10 10" fill="none" stroke="#444" stroke-width="1"><rect x=".5" y=".5" width="8" height="8"/><path d="M2.5 5l2 2 4-5"/></svg>Management</li>
    </ul>
    <ul class="abs service-list" style="left:190px">
      <li><svg class="tick" viewBox="0 0 10 10" fill="none" stroke="#444" stroke-width="1"><rect x=".5" y=".5" width="8" height="8"/><path d="M2.5 5l2 2 4-5"/></svg>Inspections</li>
      <li><svg class="tick" viewBox="0 0 10 10" fill="none" stroke="#444" stroke-width="1"><rect x=".5" y=".5" width="8" height="8"/><path d="M2.5 5l2 2 4-5"/></svg>Accounting</li>
      <li><svg class="tick" viewBox="0 0 10 10" fill="none" stroke="#444" stroke-width="1"><rect x=".5" y=".5" width="8" height="8"/><path d="M2.5 5l2 2 4-5"/></svg>HOA Compliance</li>
    </ul>

    <div class="abs contact-strip">
      <svg width="11" height="11" viewBox="0 0 24 24" fill="#fff"><path d="M6.6 10.8a15 15 0 006.6 6.6l2.2-2.2a1 1 0 011-.25 11.4 11.4 0 003.6.57 1 1 0 011 1V20a1 1 0 01-1 1A17 17 0 013 4a1 1 0 011-1h3.5a1 1 0 011 1c0 1.25.2 2.45.57 3.57a1 1 0 01-.25 1z"/></svg>
      <span>541-555-0182</span><span class="sep"></span>
      <svg width="12" height="9" viewBox="0 0 12 9" fill="none" stroke="#fff" stroke-width="1.2"><rect x=".6" y=".6" width="10.8" height="7.8"/><path d="M.6.6L6 5l5.4-4.4"/></svg>
      <span>@hollisrentalmanagement</span>
    </div>

    <svg class="abs person" width="768" height="513" viewBox="0 0 768 513" role="img" aria-label="Portrait of the company owner in black, arms crossed">
      <defs>
        <linearGradient id="personTone" x1="0" y1="0" x2="0" y2="1">
          <stop offset="0" stop-color="#4a4a4a"/>
          <stop offset="1" stop-color="#1d1d1d"/>
        </linearGradient>
      </defs>
      <path d="M392,195 C392,125 474,125 474,195 L476,250 C486,280 488,320 484,360 L476,513 L372,513 L370,420 C348,392 334,356 338,334 C344,306 370,278 390,262 Z" fill="url(#personTone)"/>
    </svg>

    <div class="abs offer">
      <p class="offer__title">OUR PROPERTY<br>MANAGEMENT</p>
      <div class="offer__rule"></div>
      <p class="offer__sub">STARTS AT <sup>$</sup>100</p>
    </div>
    <p class="abs agent">DANA HOLLIS</p>
  </div>
</section>

<!-- BACK -->
<section class="card card--back">
  <div class="card__inner">
    <svg class="shapes" width="766" height="510" viewBox="0 0 766 510">
      <defs>
        <linearGradient id="housePhoto" x1="0" y1="0" x2="1" y2="0">
          <stop offset="0" stop-color="#b9b9b2"/>
          <stop offset=".6" stop-color="#8d9a7a"/>
          <stop offset="1" stop-color="#ffffff"/>
        </linearGradient>
        <linearGradient id="houseFade" x1="0" y1="0" x2="0" y2="1">
          <stop offset="0" stop-color="#fff" stop-opacity="0"/>
          <stop offset=".75" stop-color="#fff" stop-opacity="0"/>
          <stop offset="1" stop-color="#fff" stop-opacity=".9"/>
        </linearGradient>
        <linearGradient id="circlePhotoA" x1="0" y1="0" x2="0" y2="1"><stop offset="0" stop-color="#8b96a6"/><stop offset="1" stop-color="#c9a892"/></linearGradient>
        <linearGradient id="circlePhotoB" x1="0" y1="0" x2="1" y2="1"><stop offset="0" stop-color="#d8d2cc"/><stop offset="1" stop-color="#7a6a5c"/></linearGradient>
      </defs>
      <rect x="0" y="175" width="455" height="265" fill="url(#housePhoto)" role="img" aria-label="Photo of a modern white house with wood cladding and garden hedges"/>
      <rect x="0" y="175" width="455" height="265" fill="url(#houseFade)"/>
      <polygon points="0,0 372,0 372,110 300,230 165,183 0,265" fill="var(--ink)"/>
      <circle cx="393" cy="66" r="56" fill="url(#circlePhotoA)" stroke="#8a8a8a" stroke-width="4" role="img" aria-label="Photo of hands presenting a small model house"/>
      <circle cx="358" cy="188" r="82" fill="url(#circlePhotoB)" stroke="#8a8a8a" stroke-width="4" role="img" aria-label="Photo of a contract being signed beside small model houses"/>
      <rect x="0" y="449" width="195" height="50" rx="8" fill="var(--ink)"/>
      <rect x="0" y="449" width="20" height="50" fill="var(--ink)"/>
    </svg>

    <p class="abs back-title">TIRED OF BEING THE</p>
    <ul class="abs role-list" style="left:40px">
      <li><svg class="tick" viewBox="0 0 10 10" fill="none" stroke="#ccc" stroke-width="1"><rect x=".5" y=".5" width="8" height="8"/><path d="M2.5 5l2 2 4-5"/></svg>Landlord</li>
      <li><svg class="tick" viewBox="0 0 10 10" fill="none" stroke="#ccc" stroke-width="1"><rect x=".5" y=".5" width="8" height="8"/><path d="M2.5 5l2 2 4-5"/></svg>Repairman</li>
      <li><svg class="tick" viewBox="0 0 10 10" fill="none" stroke="#ccc" stroke-width="1"><rect x=".5" y=".5" width="8" height="8"/><path d="M2.5 5l2 2 4-5"/></svg>Leasing agent</li>
    </ul>
    <ul class="abs role-list" style="left:160px">
      <li><svg class="tick" viewBox="0 0 10 10" fill="none" stroke="#ccc" stroke-width="1"><rect x=".5" y=".5" width="8" height="8"/><path d="M2.5 5l2 2 4-5"/></svg>Accountant</li>
      <li><svg class="tick" viewBox="0 0 10 10" fill="none" stroke="#ccc" stroke-width="1"><rect x=".5" y=".5" width="8" height="8"/><path d="M2.5 5l2 2 4-5"/></svg>Inspector</li>
    </ul>
    <p class="abs back-cta">WE ARE THERE<br>TO HELP</p>

    <div class="abs brand" style="left:470px;top:32px;gap:9px">
      <span class="brand__mark" style="width:32px;height:32px"></span>
      <span class="brand__name" style="font-size:30px">HOLLIS<small style="font-size:5px;letter-spacing:1.5px;margin-top:2px">PROPERTY MANAGEMENT LLC.</small></span>
    </div>
    <div class="abs stamp"></div>

    <div class="abs estimate-pill">CALL TODAY FOR A</div>
    <p class="abs estimate-label">FREE ESTIMATE</p>

    <div class="abs back-phone">
      <svg width="20" height="20" viewBox="0 0 24 24" fill="none" stroke="var(--ink)" stroke-width="2"><path d="M6.6 10.8a15 15 0 006.6 6.6l2.2-2.2a1 1 0 011-.25 11.4 11.4 0 003.6.57 1 1 0 011 1V20a1 1 0 01-1 1A17 17 0 013 4a1 1 0 011-1h3.5a1 1 0 011 1c0 1.25.2 2.45.57 3.570a1 1 0 01-.25 1z"/></svg>
      541-555-0182
    </div>
    <div class="abs back-mail">
      <svg width="14" height="10" viewBox="0 0 12 9" fill="none" stroke="var(--ink)" stroke-width="1.2"><rect x=".6" y=".6" width="10.8" height="7.8"/><path d="M.6.6L6 5l5.4-4.4"/></svg>
      @hollisrentalmanagement
    </div>
  </div>
</section>

</body>
</html>
```